Flyer für Computer Service
Zielgruppe
Privathaushalte und kleinere Firmen.
Wir möchten damit neue Kunden für unsere Dienstleistungen gewinnen.
Aufgabenstellung
Wir möchten mit diesem Flyer speziell unsere Computer Service Dienstleistungen bewerben.
Im wesentlichen werden folgende 3 Kategorieren von Dienstleistungen angeboten:
- Fernwartung
- Reparaturen
- Neuinstallationen, Backups und Virenentfernung
Fernwartung und Reparaturen bieten wir zu "ab EUR xx.-" Preisen an und Neuinstallationen, Backups und Virenentfernung zu Pauschalen.

```html
<!DOCTYPE html>
<html lang="de">
<head>
<meta charset="utf-8">
<title>Relvano – PC Probleme</title>
<link href="https://fonts.googleapis.com/css2?family=Russo+One&family=Open+Sans:wght@700;800&family=Arimo:wght@700&display=swap" rel="stylesheet">
<style>
:root{
  --orange:#f7901e;
  --orange-dark:#e0700a;
  --blue:#2f86d6;
  --blue-dark:#1d5fa8;
  --navy:#1b3f73;
  --text:#163a66;
  --grey:#4a5560;
  --white:#ffffff;
}
*{margin:0;padding:0;box-sizing:border-box}
html,body{width:849px;height:1200px;overflow:hidden;background:#fff}
.flyer{position:relative;width:849px;height:1200px;overflow:hidden;background:linear-gradient(#fff 0,#fff 380px,#e4e6e8 540px,#f4f5f6 690px,#fff 700px);font-family:"Open Sans",sans-serif}
.abs{position:absolute}
.header-bg{left:0;top:0;width:849px;height:390px}
.portrait{left:10px;top:10px;width:270px;height:300px;background:linear-gradient(160deg,#6f9fd0,#2f5f93);transform:rotate(-3deg)}
.title{left:335px;top:72px;font-family:"Russo One",sans-serif;font-size:48px;font-weight:400;color:var(--white);-webkit-text-stroke:2px var(--blue-dark);letter-spacing:1px;text-shadow:2px 3px 3px rgba(0,0,0,.35)}
.lead{right:27px;top:132px;text-align:right;color:var(--white);font-weight:800;font-size:27px;line-height:38px;text-shadow:2px 2px 3px rgba(0,0,0,.45)}
.sublead{right:27px;top:224px;text-align:right;color:var(--white);font-weight:700;font-size:19px;line-height:38px;text-shadow:1px 1px 2px rgba(0,0,0,.35)}
.sublead em{font-style:normal;color:#ffe07a}
.sublead strong{font-weight:800;font-size:22px;color:#ffe07a}
.device{left:505px;top:305px;width:330px;height:245px;background:radial-gradient(ellipse at 60% 50%,#4a4d52,#b9bcc0 75%,transparent 76%)}
.box{position:absolute;padding:14px 18px 0;border:2px solid #fff;box-shadow:0 2px 6px rgba(0,0,0,.25)}
.box.blue{background:linear-gradient(var(--blue),#5aa7e8)}
.box.orange{background:linear-gradient(var(--orange),#fbb45a)}
.box h2{font-family:"Open Sans",sans-serif;font-weight:800;font-size:19px;line-height:26px;letter-spacing:.5px;margin-bottom:12px}
.box.blue h2{color:var(--orange);text-shadow:1px 1px 0 #fff}
.box.orange h2{color:var(--blue-dark);text-shadow:1px 1px 0 #fff}
.box p{font-family:"Arimo",sans-serif;font-weight:700;font-size:11.5px;line-height:16.5px;color:var(--text)}
.price{position:absolute;left:12px;bottom:8px;height:40px;line-height:40px;white-space:nowrap;font-family:"Open Sans",sans-serif;font-weight:800;font-size:27px;color:var(--grey);text-shadow:1px 1px 0 #fff}
.price b{font-size:38px;margin-left:8px}
.blue .price b{color:var(--orange)}
.orange .price b{color:var(--blue-dark)}
.features{left:535px;top:565px;list-style:none}
.features li{font-weight:800;font-size:21px;line-height:26px;color:#fff;text-shadow:1px 2px 2px rgba(0,0,0,.6);padding-left:30px;position:relative}
.features li::before{content:"";position:absolute;left:2px;top:8px;width:12px;height:12px;background:var(--orange);border:2px solid #fff}
.footer{left:0;top:966px;width:849px;height:234px}
.brand{left:55px;top:1010px;font-family:"Russo One",sans-serif;font-size:96px;line-height:1;color:var(--orange);letter-spacing:-1px}
.web{left:282px;top:1113px;font-weight:800;font-size:19px;color:#fff}
.web span{color:var(--orange)}
.address{left:57px;top:1150px;font-weight:700;font-size:16px;color:#fff}
.contact{left:555px;top:1058px;transform:rotate(-13deg);transform-origin:left top;color:var(--blue-dark);font-weight:800;text-shadow:1px 1px 0 #fff}
.contact .label{font-size:24px}
.contact .phone{font-size:34px;line-height:38px}
.contact .mail{font-size:16px}
</style>
</head>
<body>
<div class="flyer">
  <svg class="abs header-bg" viewBox="0 0 849 390" aria-hidden="true">
    <defs>
      <linearGradient id="hdrOrange" x1="0" y1="0" x2="1" y2="1">
        <stop offset="0" stop-color="#f59a2a"/><stop offset="1" stop-color="#f07a10"/>
      </linearGradient>
    </defs>
    <polygon points="0,0 310,0 290,300 0,330" fill="#2f7fcf"/>
    <polygon points="290,22 849,6 849,385 0,385 0,330 270,300" fill="url(#hdrOrange)"/>
    <path d="M340,385 C470,250 640,200 849,210 L849,250 C660,245 510,290 410,385Z" fill="#fbb04f" opacity=".45"/>
    <path d="M560,130 C650,60 760,40 849,45 L849,80 C760,80 680,100 600,150Z" fill="#fbb04f" opacity=".35"/>
  </svg>
  <div class="abs portrait" role="img" aria-label="Foto eines Technikers im Anzug mit Laptop"></div>

  <h1 class="abs title">PC PROBLEME ???</h1>
  <p class="abs lead">..kein Problem, wir helfen Ihnen Sofort<br>Professinal, Schnell und Günstig</p>
  <p class="abs sublead">Lassen Sie sich von unserem <em>Fachpersonal</em> <strong>Beraten</strong><br>und von unseren <em>Profis</em> <strong>Helfen</strong></p>

  <div class="abs device" role="img" aria-label="Foto von Laptop, Tastatur und PC-Tower"></div>

  <section class="box blue" style="left:8px;top:405px;width:248px;height:267px">
    <h2>REPERATUREN</h2>
    <p>Hier könnte ihr Feintext stehen der Ihre Leistung genau erklährt. Hier könnte ihr Feintext stehen der Ihre Leistung genau erklährt. Hier könnte ihr Feintext stehen der Ihre Leistung genau erklährt.der Ihre Leistung genau erklährt. Hier könnte ihr Feintext stehen der Ihre Leistung genau</p>
    <div class="price">schon ab <b>59 €</b></div>
  </section>
  <section class="box orange" style="left:267px;top:405px;width:244px;height:267px">
    <h2>FERNWARTUNG</h2>
    <p>Hier könnte ihr Feintext stehen der Ihre Leistung genau erklährt. Hier könnte ihr Feintext stehen der Ihre Leistung genau erklährt. Hier könnte ihr Feintext stehen der Ihre Leistung genau erklährt.der Ihre Leistung genau erklährt. Hier könnte ihr Feintext stehen der Ihre Leistung genau</p>
    <div class="price">schon ab <b>59 €</b></div>
  </section>

  <ul class="abs features">
    <li>Schneller Service</li>
    <li>Fixe Tiefpreise</li>
    <li>Kompetente Beratung</li>
    <li>Professioneller Support</li>
  </ul>

  <section class="box orange" style="left:8px;top:694px;width:274px;height:268px">
    <h2>NEUINSTALLATIONEN</h2>
    <p>Hier könnte ihr Feintext stehen der Ihre Leistung genau erklährt. Hier könnte ihr Feintext stehen der Ihre Leistung genau erklährt. Hier könnte ihr Feintext stehen der Ihre Leistung genau erklährt. Hier könnte ihr Feintext der Ihre Leistung genau erklährt. Hier könnte ihr Feintext stehen der Ihre Leistung genau</p>
    <div class="price">schon ab <b>59 €</b></div>
  </section>
  <section class="box blue" style="left:300px;top:694px;width:262px;height:268px">
    <h2>BACKUPS</h2>
    <p>Hier könnte ihr Feintext stehen der Ihre Leistung genau erklährt. Hier könnte ihr Feintext stehen der Ihre Leistung genau erklährt. Hier könnte ihr Feintext stehen der Ihre Leistung genau erklährt. Hier könnte ihr Feintext der Ihre Leistung genau erklährt. Hier könnte ihr Feintext stehen der Ihre Leistung genau</p>
    <div class="price">schon ab <b>59 €</b></div>
  </section>
  <section class="box orange" style="left:580px;top:694px;width:258px;height:268px">
    <h2>Virenentfernung</h2>
    <p>Hier könnte ihr Feintext stehen der Ihre Leistung genau erklährt. Hier könnte ihr Feintext stehen der Ihre Leistung genau erklährt. Hier könnte ihr Feintext stehen der Ihre Leistung genau erklährt. Hier könnte ihr Feintext der Ihre Leistung genau erklährt. Hier könnte ihr Feintext stehen der Ihre Leistung genau</p>
    <div class="price">schon ab <b>59 €</b></div>
  </section>

  <svg class="abs footer" viewBox="0 0 849 234" aria-hidden="true">
    <rect width="849" height="234" fill="#2e7fd0"/>
    <polygon points="0,0 849,0 849,16 0,41" fill="#1d5fa8"/>
    <polygon points="520,234 560,66 849,16 849,234" fill="#f7901e"/>
    <polygon points="540,234 575,81 849,34 849,56 590,101 560,234" fill="#fbb04f" opacity=".5"/>
  </svg>
  <div class="abs brand">relvano</div>
  <div class="abs web">www.<span>relvano</span>.ch</div>
  <div class="abs address">Relvano GmbH - Musterstr.12 - Musterhausen 33667</div>
  <div class="abs contact">
    <div class="label">INFOS UNTER :</div>
    <div class="phone">0800 / 4455667</div>
    <div class="mail">Email : info@relvano.ch</div>
  </div>
</div>
</body>
</html>
```